Lawn maintenance
We are your green choice!
weekly , biweekly

Target Market(s)

lawn care

Industry/Entity Type

Lawn Care

Contact Information for Business Card

eye catching - not you normal "lawn business" card

Logo Text

Tall Oak Lawncare

Font styles to use
Serif
Sans Serif

Colors
ec1f27
00a990
9bcb3c
0455a3

Requirements
Must have
• Milo Hanford
• 410-555-0187
• Lawn maintenance
• We are your green choice!
• Call for a quote today!
• weekly or biweekly
Nice to have
• maybe some poker chips or playing cards
Should not have
• snow removal

```html
<!DOCTYPE html>
<html lang="en">
<head>
<meta charset="UTF-8">
<title>Tall Oak Lawncare – Business Card</title>
<link href="https://fonts.googleapis.com/css2?family=Arimo:wght@400;700&family=Roboto+Slab:wght@400&display=swap" rel="stylesheet">
<style>
  :root {
    --backdrop: #e5e5e5;
    --card-green: #17aa91;
    --ink-white: #ffffff;
  }
  html, body {
    margin: 0;
    padding: 0;
    width: 1200px;
    height: 1200px;
    overflow: hidden;
    background: var(--backdrop);
  }
  .stage {
    position: relative;
    width: 1200px;
    height: 1200px;
  }
  .card {
    position: absolute;
    left: 388px;
    top: 290px;
    width: 424px;
    height: 680px;
    border-radius: 28px;
    background: var(--card-green);
    color: var(--ink-white);
  }
  .corner {
    position: absolute;
    width: 50px;
    text-align: center;
  }
  .corner-top { left: 27px; top: 22px; }
  .corner-bottom { right: 27px; bottom: 22px; transform: rotate(180deg); }
  .rank {
    display: block;
    font-family: "Roboto Slab", serif;
    font-size: 62px;
    line-height: 56px;
    height: 56px;
  }
  .suit {
    display: block;
    width: 49px;
    height: 58px;
    margin: 4px auto 0;
  }
  .details {
    position: absolute;
    left: 86px;
    top: 215px;
    font-family: "Arimo", Arial, sans-serif;
    font-size: 26.7px;
    line-height: 32.4px;
  }
  .details p { margin: 0; }
  .company { font-weight: 700; }
  .pitch { margin-top: 16px !important; }
</style>
</head>
<body>
<div class="stage">
  <div class="card">
    <div class="corner corner-top">
      <span class="rank">A</span>
      <svg class="suit" viewBox="0 0 49 58" aria-hidden="true">
        <g fill="var(--ink-white)">
          <circle cx="24.5" cy="12" r="11.5"/>
          <circle cx="11.5" cy="31" r="11.5"/>
          <circle cx="37.5" cy="31" r="11.5"/>
          <rect x="18" y="18" width="13" height="16"/>
          <path d="M22.5 30 L26.5 30 L28 52 Q29 56 32 57 L17 57 Q20 56 21 52 Z"/>
        </g>
      </svg>
    </div>

    <div class="details">
      <p class="company">Tall Oak Lawncare</p>
      <p>Lawn maintenance</p>
      <p>Milo Hanford</p>
      <p>410-555-0187</p>
      <p class="pitch">We are your green choice!</p>
      <p>Call for a quote today!</p>
      <p>Weekly or biweekly</p>
    </div>

    <div class="corner corner-bottom">
      <span class="rank">A</span>
      <svg class="suit" viewBox="0 0 49 58" aria-hidden="true">
        <g fill="var(--ink-white)">
          <circle cx="24.5" cy="12" r="11.5"/>
          <circle cx="11.5" cy="31" r="11.5"/>
          <circle cx="37.5" cy="31" r="11.5"/>
          <rect x="18" y="18" width="13" height="16"/>
          <path d="M22.5 30 L26.5 30 L28 52 Q29 56 32 57 L17 57 Q20 56 21 52 Z"/>
        </g>
      </svg>
    </div>
  </div>
</div>
</body>
</html>
```